Flyer-Design für meine Tätigkeit als freier Trauerredner
Zielgruppe
Für meine Tatigkeit als freier Trauerredner bei Beerdigungen möchte ich einen Flyer designen lassen, um diesen bei Bestattern aufzulegen sowie diese grundsätzlich als Informationsmaterial an interessierte Personen weitergeben zu können. Zielgruppe sind einerseits Personen, die sich lange im Vorfeld Gedanken über den Tod machen und den Wunsch äußern, im Rahmen einer persönlichen Gedenkfeier, unabhängig einer Konfessionszugehörigkeit und der Kirche verabschiedet zu werden. Auf der anderen Seite ist der Flyer ebenso für trauendernde Angehörige gedacht, die aufgrund eines unerwarteten Todesfalls sich mit dem Thema Beerdigung auseinadersetzen müssen und nach Alternativen zu einer krichlichen Beerdiugung suchen.
Aufgabenstellung
Eine Visitenkarte scheint mir im Format zu klein ... ein Flyer in einem größeren Format scheint mir geeigneter, Informationen zu vermitteln. Eine große Stärke von mir ist meine Emapthie. Der Flyer soll dies in der Bildsprache ausdrücken. Ebenso soll der Flyer durch die Bilder und die gewählte Sprahce Vertrauen aufbauen. Tod und Beerdigung sind für viele ein Tabuthemen ... der Flyer soll hier eine Brücke schlagen.
Wichtig wäre mir den Ablauf der Vorbereitung im Flyer aufzuskizzieren, um zu wissen, wie die Vorbereitung und Druchführung beispielhaft erfolgt.
Meine Kernaussage:
Freie Trauerreden, so einzigartig und besonders wie jeder Mensch selbst!
Als freier Trauerredner ist es mein Anspruch, den schweren Moment des Abschiednehmens so persönlich und würdevoll wie nur möglich zu gestalten!
Mein Ziel: Herzensverbindungen zwischen Menschen aufleben zu lassen und diese zu stärken. Herzensverbindungen leben und wirken weiter – unabhängig ob im Leben oder über den Tod hinaus!
Alle Informationen, die im Flyer aufgeführt werden sollen, sind dem beigefügten Word-Dokument zu entnehmen.
Wichtige Information finden Sie auf meiner Website www.tobiaskrämer.com
Wenn ein Statement oder Reszession benötigt wird und sich gut im Flyer macht, liefere ich diese gerne nach.

```html
<!DOCTYPE html>
<html lang="de">
<head>
<meta charset="utf-8">
<title>Tobias Krämer – Freier Trauerredner – Faltflyer</title>
<link href="https://fonts.googleapis.com/css2?family=Montserrat:wght@400;500;600;700&display=swap" rel="stylesheet">
<style>
  :root{
    --bg:#e6e6e6;
    --paper:#f4f4f3;
    --slate:#62615f;
    --slate-deep:#595856;
    --slate-soft:#6a6967;
    --ink:#4a4a48;
    --white:#ffffff;
    --accent:#e6d54a;
    --cover-light:#cfd0d0;
  }
  *{box-sizing:border-box;margin:0;padding:0}
  html,body{width:1200px;height:900px;overflow:hidden}
  body{background:var(--bg);font-family:"Montserrat",sans-serif;color:var(--ink);position:relative}
  .spread{position:absolute;left:270px;width:660px;height:430px;display:flex;box-shadow:0 6px 18px rgba(0,0,0,.18)}
  .spread--outside{top:15px}
  .spread--inside{top:455px}
  .panel{position:relative;width:220px;height:430px;overflow:hidden}
  .panel svg.shape{position:absolute;inset:0;width:100%;height:100%}
  .block{position:absolute;left:14px;right:14px}
  .heading{font-weight:500;font-size:11px;line-height:1.2;letter-spacing:.02em;text-transform:uppercase}
  .body{font-size:5.6px;line-height:1.55}
  .body b{font-weight:700}
  .on-dark{color:var(--white)}
  .accent{color:var(--accent)}
  .list{list-style:none;margin-top:6px}
  .list li{display:flex;gap:8px;font-size:5.8px;line-height:1.55;margin-bottom:7px}
  .list li span.num{color:var(--accent);min-width:6px}
  .brand{font-size:11px;line-height:1.05}
  .brand strong{font-weight:700;letter-spacing:.03em}
  .brand em{font-style:normal;font-weight:400;display:block;font-size:9px;letter-spacing:.03em}
  .claim{font-size:11px;line-height:1.02;font-weight:500;color:var(--ink)}
  .rule{height:2px;width:160px;background:var(--accent);margin-bottom:8px}
</style>
</head>
<body>

<!-- Außenseite -->
<section class="spread spread--outside">

  <article class="panel panel--costs" style="background:var(--paper)">
    <svg class="shape" viewBox="0 0 220 430" preserveAspectRatio="none">
      <polygon points="0,0 220,0 220,168 0,262" fill="var(--slate)"/>
    </svg>
    <div class="block on-dark" style="top:16px">
      <h2 class="heading">Die Kosten und Dauer einer Trauerfeier:</h2>
      <p class="body" style="margin-top:4px"><b>Dauer einer freien Trauerfeier</b><br>Eine freie Trauerfeier dauert in der Regel 20 - 30 Minuten.<br><b>Kosten der Trauerrede / Gedenkfeier</b><br>Die Kosten für die Trauerrede, bzw. der Umrahmung Gedenkfeier betragen 439 EUR inkl. MwSt. Die Pauschale beinhaltet das Vorbereitungsgespräch sowie die Aufbereitung und Durchführung der freien Trauerrede, die Sie zum Nachlesen als persönliches Exemplar erhalten.<br>Die Fahrtkosten betragen 55 Cent je Kilometer für die Fahrt zum Friedhof bzw. Ort der Verabschiedung und zurück.</p>
    </div>
    <div class="block" style="top:285px">
      <h2 class="heading" style="font-size:10px">Gemeinsam...</h2>
      <p class="body" style="margin-top:4px">In die belebende Kraft und spürbare Freiheit gehen.</p>
      <p class="body" style="margin-top:8px">Effektive Antworten und erfolgsversprechende Lösungen finden.</p>
      <p class="body" style="margin-top:8px">Neue Perspektiven und Möglichkeiten erschließen.</p>
    </div>
  </article>

  <article class="panel panel--contact" style="background:var(--paper)">
    <svg class="shape" viewBox="0 0 220 430" preserveAspectRatio="none">
      <defs>
        <linearGradient id="lakeTone" x1="0" y1="0" x2="1" y2="1">
          <stop offset="0" stop-color="#d9d6d0"/>
          <stop offset=".5" stop-color="#b7b3ac"/>
          <stop offset="1" stop-color="#8e8b86"/>
        </linearGradient>
      </defs>
      <polygon role="img" aria-label="Foto: Mann am Seeufer im Abendlicht" points="0,220 220,150 220,275 0,245" fill="url(#lakeTone)"/>
      <polygon points="0,240 220,280 220,430 0,430" fill="var(--slate)"/>
    </svg>
    <div class="block" style="top:16px">
      <h2 class="heading">Vereinbaren Sie jetzt ein kostenloses Erstgespräch!</h2>
      <p class="body" style="margin-top:5px;padding-right:20px">Freier Trauerredner zu sein ist meine Berufung! Mir ist es eine Freude, Menschen Halt und Kraft zu geben! Das ist mein Anspruch – sowohl als freier Trauerredner im Moment des Abschiednehmens, aber auch als Coach, wenn es darum geht, wieder Halt und Kraft im Leben zu finden!</p>
    </div>
    <div class="block on-dark" style="top:283px">
      <p style="font-size:8px;line-height:1;padding-left:36px;letter-spacing:.03em">TOBIAS<br>KRÄMER</p>
      <p style="font-size:8px;margin-top:14px;letter-spacing:.04em">WWW.TOBIASKRÄMER.COM</p>
      <p class="body" style="margin-top:14px">Am Birkenhang 7 I 94400 Musterau<br>E-Mail: info@tobiaskrämer.com<br>Tel./WhatsApp/Telegramm: 0170 4418260</p>
    </div>
  </article>

  <article class="panel panel--cover" style="background:var(--cover-light)">
    <svg class="shape" viewBox="0 0 220 430" preserveAspectRatio="none">
      <defs>
        <linearGradient id="portraitTone" x1="0" y1="0" x2="1" y2="1">
          <stop offset="0" stop-color="#c9c3b8"/>
          <stop offset=".45" stop-color="#e4dccd"/>
          <stop offset="1" stop-color="#a99f92"/>
        </linearGradient>
      </defs>
      <polygon role="img" aria-label="Foto: Porträt des Trauerredners vor Seekulisse" points="0,170 220,65 220,300 180,430 0,430" fill="url(#portraitTone)"/>
      <polygon points="220,280 220,430 168,430" fill="var(--slate)"/>
    </svg>
    <div class="block brand" style="top:42px;color:var(--ink)">
      <strong>TOBIAS KRÄMER</strong>
      <em>FREIER TRAUERREDNER</em>
    </div>
    <p class="block claim" style="top:298px">Freie Gedenkfeiern, so einzigartig und besonders wie jeder Mensch selbst!</p>
  </article>
</section>

<!-- Innenseite -->
<section class="spread spread--inside">

  <article class="panel panel--process" style="background:var(--slate)">
    <div class="block on-dark" style="top:16px">
      <h2 class="heading accent">Vorbereitung/Ablauf:</h2>
      <ol class="list">
        <li><span class="num">1.</span><span>ÜBERLEGUNGEN IM VORFELD: Es ist gut, im ersten Schritt der Planung einer freien Trauerfeier grundsätzlichen Überlegungen Raum zu geben, wie zum Beispiel: <span class="accent">Hat die/der Verstorbene im Vorfeld Wünsche zur eigenen Beerdigung geäußert?</span> Wie sollte die freie Trauerfeier ablaufen, damit die Gedenkfeier „stimmig“ ist – für die verstorbene Person, Sie selbst, Familie, Freunde und sie diese später in guter Erinnerung behalten?</span></li>
        <li><span class="num">2.</span><span>DAS VORBEREITUNGSGESPRÄCH – Dauer ca. 2 Stunden. Persönlich, telefonisch oder digital werden in einem Vorbereitungsgespräch alle wichtigen Informationen zur verstorbenen Person gesammelt und gemeinsam der Ablauf der freien Gedenkfeier geplant.</span></li>
        <li><span class="num">3.</span><span>Ablauf der Gedenkfeier – Dauer ca. 20 – 30 Minuten. Den Möglichkeiten des Ablaufs einer freien Trauerfeier sind wenig Grenzen gesetzt – Ihre Bedürfnisse und Wünsche stehen im Mittelpunkt!</span></li>
      </ol>
    </div>
    <div role="img" aria-label="Foto: Waldlichtung mit hellen Bändern im Gegenlicht" style="position:absolute;left:0;right:0;bottom:0;height:112px;background:linear-gradient(160deg,#c9c6b9 0%,#7a6f55 40%,#4f4636 100%)"></div>
  </article>

  <article class="panel panel--elements" style="background:var(--slate-deep)">
    <div class="block on-dark" style="top:14px">
      <div class="rule"></div>
      <h2 class="heading">Wichtige Elemente:</h2>
      <p class="body" style="margin-top:5px">Persönliche Worte in Form einer individuellen Trauerrede zur Würdigung des Lebens der verstorbenen Person. Ausgewählte Musikstücke. Aktive Beteiligung Ihrerseits, von Angehörigen und/oder Freunden durch das Vorlesen eines Gedichts, eines Gebets oder persönlich verfasster Worte.<br>Rituale des Gedenkens können einen würdevollen, persönlichen Beitrag umrahmen und in verschiedenster Weise integriert werden, z.B. Seifenblasen, Briefe/Wünsche, eine Lichterkranz der Verbundenheit oder Wunderkerzen zum Schluss einer Gedenkfeier, um symbolisch Sterne der Liebe und Dankbarkeit regnen zu lassen.</p>
    </div>
    <div role="img" aria-label="Foto: Bauernhaus mit Holzgiebel im hellen Licht" style="position:absolute;left:14px;right:14px;top:212px;height:66px;background:linear-gradient(170deg,#f3efe8 0%,#d9cfc0 55%,#a89886 100%)"></div>
    <div class="block on-dark" style="top:292px">
      <h3 style="font-size:7.5px;font-weight:500;letter-spacing:.03em">ORTE FÜR FREIE TRAUERFEIERN:</h3>
      <p class="body" style="margin-top:7px">Freie Trauerfeiern finden meist auf Friedhöfen, in Kapellen oder Aussegnungshallen, auf dem Friedhofsgelände, einem Waldfriedhof oder auch in den eigenen Räumen des Bestatters statt. Auch ein selbstgewählter Ort in der Natur kann unter bestimmten Voraussetzungen möglich sein.</p>
    </div>
  </article>

  <article class="panel panel--about" style="background:var(--slate-soft)">
    <div style="position:absolute;left:0;right:0;top:0;height:128px;background:var(--paper)"></div>
    <div class="block" style="top:16px">
      <h2 class="heading">Was ist eine freie Trauer/Gedenkrede?</h2>
      <p class="body" style="margin-top:4px">Freie Trauerzeremonie, Gedenkfeier, Beerdigung, Lebensabschiedsfeier... Synonyme für eine, von mir als freier Trauerredner durchgeführte, Abschiedszeremonie, die ganz individuell und persönlich auf die verstorbene Person oder das verstorbene Kind bezogen ist - weltlich frei, unabhängig einer Konfession mit individuellem Ablauf.</p>
    </div>
    <div class="block on-dark" style="top:142px">
      <p class="accent" style="font-size:6.6px;line-height:1.4">Eine freie Trauerzeremonie beinhaltet im Wesentlichen folgende Elemente:</p>
      <ol class="list">
        <li><span class="num">1.</span><span>Gedenken an die verstorbene Person in einem feierlichen Rahmen</span></li>
        <li><span class="num">2.</span><span>Herausstellen der einzigartigen Persönlichkeit und den Charakter der Person – würdevoll wird dies in den Mittelpunkt der Feier gestellt.</span></li>
        <li><span class="num">3.</span><span>Aufleben lassen wertvoller Erinnerungen und Ausdruck der Dankbarkeit an die gemeinsamen Stunden und damit Stärkung der Herzensverbindung</span></li>
        <li><span class="num">4.</span><span>der Trauer Raum zu geben und die freie Trauerfeier Bestandteil des Aufarbeitungsprozesses werden zu lassen</span></li>
        <li><span class="num">5.</span><span>Beistand, Trost und Zuspruch erfahren - durch die anwesenden Trauergäste, den freien Trauerredner, alles Verbindende und/oder das Göttliche</span></li>
      </ol>
    </div>
  </article>
</section>

</body>
</html>
```